Amberline Picture Works Web Design

COMPANY: AMBERLINE PICTURE WORKS
LOCATION: SHANGHAI, CHINA
AREA: FILM/TV DRAMA/COMMERCIALS/GAME POST PRODUCTION, SOUND DESIGN, MUSIC, and GAME.
WEB STYLE: SIMPLE, PROFESSIONAL, TRUSTWORTHY

LANGUAGE: ENGLISH, CHINESE. (Same layout, different language)
UPDATE: AFTER PROJECT FINISHED, WE NEED UPDATE BY OURSELVES.

MAIN SUBJECT: 6
1 HOMEPAGE
2 ABOUT US
3 TEAM
4 SERVICES
5 FACILITY
6 CONTACT

add one page of JOB OPPORTUNITIES.

DETAILS
1 HOMEPAGE
SLOGAN: Amberline Picture Works provides a well-designed working environment which amplifies your team’s ability to reach their creative goals.

Our services include:
 Feature Films
 Music & Scoring
 Commercials
 ADR & Foley
 Sound & Picture Editorial
 Sound Design
 Video Game

2 ABOUT US
Amberline Picture Works is located in the premiere South-Bund area of Shanghai. Occupying a 5000 square meter Technical Building, Amberline Picture Works was built by a filmmaker for filmmakers, and is one of the largest, most versatile full-service post-production facilities in China.

Amberline Picture Works is positioning to be at the forefront of the latest technology. Our goal is to provide a comprehensive solution for the post-production needs of our clients. We offer two fully-equipped dubbing stages (one of which will be certified VORTAN SPHERA ELITE), a large variety of both picture and sound editing rooms, impressive Foley and ADR stages, a world-class scoring stage, and complete audio and video transfer services.

We can handle your entire project from editing all the way to the end of the final sound mix; all under one extremely comfortable roof. We fully realize that the true art is in listening to the needs of our clients and making their greatest vision a reality. To this end our creative team's expertise, with a network of sound supervisors, editors and mixers, will deliver the magic you need. Producers and directors will also find our richly appointed guest accommodations to be a comfortable and soothing place to wind up the day. Every aspect of your project will be taken care of by a skilled and dedicated team, in the way that is best suited to you.

3 TEAM
(attachment 01)

4 SERVICES
Sound Mix
ADR
FOLEY
MUSIC
Sound Design
Sound Edit
Picture Edit
for all the Films, TV Drama, Commercials, Video Games, Online Media
(attachment 02, use photo)

5 FACILITY
(attachment 03)

6 CONTACT
(attachment04)
with map

Reason: Designers work are great, my bosses will spend 1-2 days select one of these web design, and spend 1-2 days to make some change, maybe use new photos.

```html
<!DOCTYPE html>
<html lang="en">
<head>
<meta charset="utf-8">
<title>Amberline Picture Works</title>
<link href="https://fonts.googleapis.com/css2?family=Roboto:wght@300;400;500;700&display=swap" rel="stylesheet">
<style>
:root{
  --red:#e8323a;
  --red-dark:#b8232a;
  --teal:#1d5269;
  --teal-dark:#173f52;
  --ink:#333;
  --muted:#666;
  --line:#d6d6d6;
  --grey:#ececec;
  --grey-2:#e4e4e4;
  --footer:#2e2e2e;
  --white:#fff;
}
*{box-sizing:border-box;margin:0;padding:0}
html,body{width:1200px;height:2549px;overflow:hidden}
body{font-family:"Roboto",Arial,sans-serif;color:var(--ink);background:var(--white);position:relative;font-size:12.5px;line-height:1.45}
section,header,footer{position:absolute;left:0;width:1200px}
.abs{position:absolute}
.btn{position:absolute;background:var(--red);color:var(--white);font-size:11.5px;font-weight:500;height:30px;line-height:30px;padding:0 18px;border-radius:2px;border-bottom:2px solid var(--red-dark)}
.sec-title{position:absolute;font-size:28px;font-weight:400;color:#222;white-space:nowrap;display:flex;align-items:center}
.sec-title b{color:var(--teal);font-weight:700;margin-left:8px}
.sec-title .rule{height:1px;background:var(--line);margin-left:14px}

/* header */
.site-header{top:0;height:113px}
.brand{left:174px;top:18px;display:flex;align-items:center;gap:10px}
.brand-mark{width:30px;height:30px;background:var(--red);border-radius:50%}
.brand-name{font-size:22px;font-weight:500;color:var(--teal);line-height:1}
.search{left:484px;top:8px;width:368px;height:26px;border:1px solid var(--line);border-radius:3px;font-size:11px;color:#aaa;padding:5px 10px}
.search svg{position:absolute;right:8px;top:6px}
.account{left:862px;top:0;width:166px;height:30px;background:var(--teal);color:var(--white);font-size:13px;text-align:center;line-height:28px;clip-path:polygon(0 0,100% 0,92% 100%,8% 100%)}
.flags{left:976px;top:40px;display:flex;gap:4px}
.flags span{width:12px;height:8px;background:var(--red)}
.flags span+span{background:#3a5ea8}
.main-nav{left:436px;top:74px;display:flex;gap:0;font-size:13.5px}
.main-nav a{display:block;height:30px;line-height:30px;padding:0 14px;color:#222;text-decoration:none;border-right:1px solid var(--line)}
.main-nav a:last-child{border-right:0}
.main-nav a.active{background:var(--red);color:var(--white);border-radius:2px}

/* hero */
.hero{top:113px;height:372px;background:linear-gradient(100deg,#3b3530 0%,#5a4d44 30%,#2d3036 60%,#1c2230 100%)}
.play{left:548px;top:135px;width:104px;height:104px;border-radius:50%;background:var(--red);border:6px solid #fff}
.play svg{position:absolute;left:32px;top:26px}
.slide-arrow{top:168px;width:34px;height:34px;border-radius:50%;background:rgba(255,255,255,.55)}

/* welcome */
.welcome{top:485px;height:319px}
.welcome p{position:absolute;left:174px;width:506px;font-size:11.5px;color:#444}
.arrival-photo{left:716px;top:83px;width:169px;height:147px;background:linear-gradient(135deg,#2a2a2a,#6b6b6b 60%,#3a3a3a)}
.arrival-text{left:893px;top:83px;width:135px;font-size:11px;color:#555}
.arrival-text h4{font-size:11px;color:#222;font-weight:700;margin-bottom:2px}
.pager{top:40px;display:flex;gap:4px;left:976px}
.pager span{width:22px;height:22px;background:var(--teal);position:relative}
.pager span:first-child{background:var(--red)}

/* services */
.services{top:804px;height:516px;background:linear-gradient(180deg,#e8e8e8,#f1f1f1)}
.svc{position:absolute;width:300px}
.svc h3{font-size:19px;font-weight:700;color:#222;line-height:1.2}
.svc p{font-size:11.5px;color:#444;line-height:1.3;margin-top:4px}
.svc.left{text-align:right}
.svc-icon{position:absolute;width:94px;height:94px;border-radius:50%;background:var(--teal);border:4px solid #fff;box-shadow:0 0 0 1px #ccc}
.svc-icon svg{position:absolute;left:22px;top:22px}
.svc-center{position:absolute;left:470px;top:110px;width:260px;height:270px;display:flex;align-items:center;justify-content:center;text-align:center;font-size:30px;font-weight:700;color:var(--teal);line-height:1.2}

/* posts */
.posts{top:1320px;height:490px}
.post{position:absolute;left:174px;width:488px;height:150px;background:#f3f3f3;box-shadow:0 1px 2px rgba(0,0,0,.25)}
.post-head{height:34px;background:var(--red);color:#fff;font-size:18px;line-height:34px;padding-left:16px;position:relative}
.post-head span{position:absolute;right:0;top:0;height:34px;width:66px;background:var(--teal);font-size:11.5px;text-align:center}
.post-photo{position:absolute;left:16px;top:54px;width:142px;height:78px;background:linear-gradient(135deg,#3c4a5a,#8a8f96 55%,#2c3138)}
.post-body{position:absolute;left:172px;top:54px;width:300px;font-size:11px;color:#444;line-height:1.35}
.post-body b{color:#222}
.post-meta{position:absolute;left:172px;top:118px;width:300px;font-size:11px;color:#555;font-style:italic;border-top:1px solid var(--line);padding-top:4px}
.post-meta span{position:absolute;right:0;color:var(--red);font-style:normal}
.rank{position:absolute;left:716px;width:312px;height:62px;background:#e9e9e9;border-bottom:3px solid var(--red)}
.rank-num{position:absolute;left:0;top:0;width:60px;height:59px;background:var(--teal);color:#fff;font-size:28px;font-weight:700;line-height:59px;padding-left:14px}
.rank-avatar{position:absolute;left:62px;top:8px;width:44px;height:44px;border-radius:50%;background:#c9b9a8;border:3px solid #fff}
.rank-title{position:absolute;left:114px;top:12px;font-size:12px;font-weight:700;color:#222;text-decoration:underline;line-height:1.25}

/* testimonials */
.voices{top:1810px;height:429px;background:var(--grey)}
.quote{position:absolute;top:105px;width:264px;height:128px;background:#fff;border:1px solid var(--line);border-radius:10px;padding:14px 22px;font-size:11.5px;color:#666;line-height:1.4}
.person{position:absolute;top:250px;display:flex;align-items:center;gap:18px;font-size:11.5px;color:#666}
.person i{display:block;width:64px;height:64px;border-radius:50%;background:#cbbfb3;border:3px solid #fff}

/* social band */
.connect{top:2239px;height:64px;background:var(--teal)}
.connect-lead{left:174px;top:10px;width:250px;color:#fff;font-size:16px;font-weight:500;line-height:1.25}
.social{left:484px;top:20px;display:flex;gap:38px;color:#fff;font-size:13px}
.social span{display:flex;align-items:center;gap:10px}
.social i{width:26px;height:26px;border-radius:50%;background:#fff;display:block}

/* footer */
.site-footer{top:2303px;height:191px;background:var(--footer);color:#ccc;font-size:11.5px}
.site-footer h5{font-size:16px;font-weight:400;color:#fff;margin-bottom:12px}
.foot-col{position:absolute;top:22px}
.foot-col li{list-style:none;line-height:1.55;padding-left:12px;position:relative}
.foot-col li::before{content:"";position:absolute;left:0;top:6px;width:5px;height:5px;background:var(--red)}
.contact-row{display:flex;gap:12px;align-items:flex-start;margin-bottom:8px;line-height:1.3}
.contact-row svg{flex:none;margin-top:1px}
.subscribe-input{width:208px;height:30px;background:#fff;color:#999;padding:7px 8px;margin:10px 0 8px}
.subscribe-btn{display:inline-block;border:1px solid #ccc;color:#fff;padding:4px 8px;vertical-align:top;margin-right:10px}
.copyright{top:2494px;height:55px;background:var(--red);color:#fff;text-align:center;line-height:55px;font-size:11.5px}
</style>
</head>
<body>

<header class="site-header">
  <div class="brand abs"><span class="brand-mark"></span><span class="brand-name">Amberline Picture Works</span></div>
  <div class="search abs">Search...
    <svg width="13" height="13" viewBox="0 0 13 13"><circle cx="5.5" cy="5.5" r="4" fill="none" stroke="#e8323a" stroke-width="2"/><line x1="8.5" y1="8.5" x2="12" y2="12" stroke="#e8323a" stroke-width="2"/></svg>
  </div>
  <div class="account abs">Login | Register</div>
  <div class="flags abs"><span></span><span></span></div>
  <nav class="main-nav abs">
    <a class="active">Home</a><a>About Us</a><a>Team</a><a>Services</a><a>Facility</a><a>Job Opperturnity</a><a>Contact</a>
  </nav>
</header>

<section class="hero" role="img" aria-label="Sound engineer working at a mixing console in a studio">
  <div class="play abs"><svg width="44" height="52" viewBox="0 0 44 52"><polygon points="4,2 42,26 4,50" fill="#3a0d0f"/></svg></div>
  <div class="slide-arrow abs" style="left:26px"><svg width="34" height="34"><polyline points="20,11 13,17 20,23" fill="none" stroke="#333" stroke-width="2"/></svg></div>
  <div class="slide-arrow abs" style="left:1140px"><svg width="34" height="34"><polyline points="14,11 21,17 14,23" fill="none" stroke="#333" stroke-width="2"/></svg></div>
</section>

<section class="welcome">
  <h2 class="sec-title" style="left:174px;top:36px">Welcome to Amberline<b>Picture Works</b><span class="rule" style="width:20px"></span></h2>
  <p style="top:82px">Duis a metus consequat, placerat nibh semper, suscipit lectus. Mauris id nunc a eros bibendum ultrices. Suspendisse scelerisque scelerisque elit, vel fringilla dui pharetra non. Etiam tincidunt vitae nisi eget sodales. Morbi vel odio vitae turpis hendrerit viverra quis at erat. Maecenas viverra eleifend augue, et vehicula nisl pharetra eget. Curabitur vitae consequat tellus. Integer mollis at urna ac interdum.</p>
  <p style="top:180px">Duis commodo ante nec nisi fringilla, in facilisis massa placerat. Vivamus convallis lectus nec pharetra bibendum. Nulla fringilla magna quam, vitae facilisis risus adipiscing eget. Morbi et congue velit, eu gravida lorem. Nam non lectus id dui aliquam suscipit vitae quis sapien. Pellentesque et metus turpis.</p>
  <span class="btn" style="left:580px;top:253px">View more »</span>

  <h2 class="sec-title" style="left:716px;top:36px">Recent<b>Arrival</b><span class="rule" style="width:40px"></span></h2>
  <div class="pager abs">
    <span><svg width="22" height="22"><polyline points="13,7 9,11 13,15" fill="none" stroke="#fff" stroke-width="2"/></svg></span>
    <span><svg width="22" height="22"><polyline points="9,7 13,11 9,15" fill="none" stroke="#fff" stroke-width="2"/></svg></span>
  </div>
  <div class="arrival-photo abs" role="img" aria-label="Engineer listening on headphones at a studio desk"></div>
  <div class="arrival-text abs"><h4>DUIS COMMODO ANTE</h4>Vivamus convallis lectus nec pharetra bibendum. Nulla fringilla magna quam, vitae facilisis risus adipiscing eget. Morbi et congue velit, eu gravida lorem</div>
  <span class="btn" style="left:928px;top:253px">View more »</span>
</section>

<section class="services">
  <h2 class="sec-title" style="left:522px;top:32px;font-size:27px">Our<b>Services</b></h2>

  <div class="svc left" style="left:36px;top:102px"><h3>Feature Films</h3><p>Duis a metus consequat,<br>placerat nibh semper,<br>suscipit lectus.</p></div>
  <div class="svc-icon" style="left:351px;top:86px"><svg width="42" height="42" viewBox="0 0 42 42"><circle cx="21" cy="21" r="18" fill="none" stroke="#fff" stroke-width="3"/><circle cx="21" cy="10" r="4" fill="#fff"/><circle cx="21" cy="32" r="4" fill="#fff"/><circle cx="10" cy="21" r="4" fill="#fff"/><circle cx="32" cy="21" r="4" fill="#fff"/></svg></div>

  <div class="svc left" style="left:36px;top:222px"><h3>Music &amp; Scoring</h3><p>Duis a metus consequat,<br>placerat nibh semper,<br>suscipit lectus.</p></div>
  <div class="svc-icon" style="left:351px;top:206px"><svg width="42" height="42" viewBox="0 0 42 42"><path d="M3 8h14l3 4h19v26H3z" fill="none" stroke="#fff" stroke-width="3"/><path d="M24 17v12a3 3 0 1 1-2-2.8V19l-5 1" fill="none" stroke="#fff" stroke-width="2.5"/></svg></div>

  <div class="svc left" style="left:36px;top:336px"><h3>Commercials</h3><p>Duis a metus consequat,<br>placerat nibh semper,<br>suscipit lectus.</p></div>
  <div class="svc-icon" style="left:351px;top:320px"><svg width="42" height="42" viewBox="0 0 42 42"><polygon points="4,16 12,16 30,6 30,36 12,26 4,26" fill="#fff"/><rect x="10" y="26" width="5" height="10" fill="#fff"/><line x1="34" y1="21" x2="40" y2="21" stroke="#fff" stroke-width="2.5"/></svg></div>

  <div class="svc-center" role="img" aria-label="Amberline Picture Works">Amberline<br>Picture Works</div>

  <div class="svc-icon" style="left:753px;top:86px"><svg width="42" height="42" viewBox="0 0 42 42"><path d="M6 26V21a15 15 0 0 1 30 0v5" fill="none" stroke="#fff" stroke-width="3"/><rect x="3" y="24" width="9" height="14" rx="3" fill="#fff"/><rect x="30" y="24" width="9" height="14" rx="3" fill="#fff"/></svg></div>
  <div class="svc" style="left:858px;top:102px"><h3>ADR &amp; Foley</h3><p>Duis a metus consequat,<br>placerat nibh semper,<br>suscipit lectus.</p></div>

  <div class="svc-icon" style="left:753px;top:206px"><svg width="42" height="42" viewBox="0 0 42 42"><g stroke="#fff" stroke-width="2.5" stroke-linecap="round"><line x1="3" y1="18" x2="3" y2="24"/><line x1="8" y1="12" x2="8" y2="30"/><line x1="13" y1="6" x2="13" y2="36"/><line x1="18" y1="14" x2="18" y2="28"/><line x1="23" y1="3" x2="23" y2="39"/><line x1="28" y1="10" x2="28" y2="32"/><line x1="33" y1="15" x2="33" y2="27"/><line x1="38" y1="19" x2="38" y2="23"/></g></svg></div>
  <div class="svc" style="left:858px;top:214px"><h3>Sound &amp; Picture<br>Editorial</h3><p>Duis a metus consequat,<br>placerat nibh</p></div>

  <div class="svc-icon" style="left:753px;top:320px"><svg width="42" height="42" viewBox="0 0 42 42"><rect x="7" y="3" width="28" height="36" rx="3" fill="none" stroke="#fff" stroke-width="3"/><circle cx="21" cy="25" r="7" fill="none" stroke="#fff" stroke-width="3"/><circle cx="21" cy="11" r="2.5" fill="#fff"/></svg></div>
  <div class="svc" style="left:858px;top:336px"><h3>Sound Design</h3><p>Duis a metus consequat,<br>placerat nibh semper,<br>suscipit lectus.</p></div>

  <span class="btn" style="left:550px;top:448px">View more »</span>
</section>

<section class="posts">
  <h2 class="sec-title" style="left:174px;top:34px">Our Latest<b>Posts</b><span class="rule" style="width:174px"></span></h2>
  <div class="post" style="top:84px">
    <div class="post-head">Vivamus convallis lectus nec pharetra<span>View more</span></div>
    <div class="post-photo" role="img" aria-label="Film still of armoured warrior on a battlefield"></div>
    <div class="post-body"><b>Praesent vitae eleifend sap</b> ien, nec suscipit arcuDon ec ac nunc sed arcu rutrum gra vida. Interdum et malesuad Duis a metus consequat, placerat ...</div>
    <div class="post-meta">22 June 2014<span>8 comments</span></div>
  </div>
  <div class="post" style="top:257px">
    <div class="post-head">Vivamus convallis lectus nec pharetra<span>View more</span></div>
    <div class="post-photo" role="img" aria-label="Film still of a group of people in a dim street"></div>
    <div class="post-body"><b>Praesent vitae eleifend sap</b> ien, nec suscipit arcuDon ec ac nunc sed arcu rutrum gra vida. Interdum et malesuad Duis a metus consequat, placerat ...</div>
    <div class="post-meta">22 June 2014<span>8 comments</span></div>
  </div>
  <span class="btn" style="left:596px;top:440px">View all »</span>

  <h2 class="sec-title" style="left:716px;top:34px">Top Ranking<b>Music</b><span class="rule" style="width:40px"></span></h2>
  <div class="rank" style="top:84px"><span class="rank-num">01</span><span class="rank-avatar" role="img" aria-label="Artist portrait"></span><span class="rank-title">Aliquam eget metus a odio<br>posuere</span></div>
  <div class="rank" style="top:148px"><span class="rank-num">02</span><span class="rank-avatar" role="img" aria-label="Artist portrait"></span><span class="rank-title">Aliquam eget metus a odio<br>posuere</span></div>
  <div class="rank" style="top:212px"><span class="rank-num">03</span><span class="rank-avatar" role="img" aria-label="Artist portrait"></span><span class="rank-title">Aliquam eget metus a odio<br>posuere</span></div>
  <div class="rank" style="top:276px"><span class="rank-num">04</span><span class="rank-avatar" role="img" aria-label="Artist portrait"></span><span class="rank-title">Aliquam eget metus a odio<br>posuere</span></div>
  <div class="rank" style="top:340px"><span class="rank-num">05</span><span class="rank-avatar" role="img" aria-label="Artist portrait"></span><span class="rank-title">Aliquam eget metus a odio<br>posuere</span></div>
  <span class="btn" style="left:928px;top:440px">View more »</span>
</section>

<section class="voices">
  <div class="abs" style="left:174px;top:50px;width:854px;display:flex;align-items:center;gap:16px">
    <span style="flex:1;height:1px;background:var(--line)"></span>
    <h2 style="font-size:28px;font-weight:400;color:#222;white-space:nowrap">What User says <b style="color:var(--teal)">About Us</b></h2>
    <span style="flex:1;height:1px;background:var(--line)"></span>
  </div>
  <div class="quote" style="left:187px">Phasellus nec dui ut sapien lacinia ornare nec vel nulla. Duis vitae est vel magna im pe rdiet aliquet. Morbi justo augue, conv allis vel scelerisque nec, dapibus porta ligula. Quisque a dictum diam. Nulla tristique</div>
  <div class="quote" style="left:466px">Phasellus nec dui ut sapien lacinia ornare nec vel nulla. Duis vitae est vel magna im pe rdiet aliquet. Morbi justo augue, conv allis vel scelerisque nec, dapibus porta ligula. Quisque a dictum diam. Nulla tristique</div>
  <div class="quote" style="left:745px">Phasellus nec dui ut sapien lacinia ornare nec vel nulla. Duis vitae est vel magna im pe rdiet aliquet. Morbi justo augue, conv allis vel scelerisque nec, dapibus porta ligula. Quisque a dictum diam. Nulla tristique</div>
  <div class="person" style="left:206px"><i role="img" aria-label="Client portrait"></i>Volutpat semper</div>
  <div class="person" style="left:500px"><i role="img" aria-label="Client portrait"></i>Dignissim imperdiet</div>
  <div class="person" style="left:794px"><i role="img" aria-label="Client portrait"></i>Integer blandit</div>
  <span class="btn" style="left:562px;top:358px">View all »</span>
</section>

<section class="connect">
  <div class="connect-lead abs">Stay connected with us in your favorite flavor! »</div>
  <div class="social abs">
    <span><i></i>Friendwall</span><span><i></i>Chirpline</span><span><i></i>Workrank</span><span><i></i>Circlecast</span>
  </div>
</section>

<footer class="site-footer">
  <div class="foot-col" style="left:178px;width:200px">
    <h5>Kontactinfo</h5>
    <div class="contact-row"><svg width="14" height="14" viewBox="0 0 14 14"><polygon points="7,1 13,7 11,7 11,13 3,13 3,7 1,7" fill="#fff"/></svg><span>200 Nullam auctor sit amet<br>lorem ac condimentum.</span></div>
    <div class="contact-row"><svg width="14" height="14" viewBox="0 0 14 14"><path d="M3 1l3 3-2 2a8 8 0 0 0 4 4l2-2 3 3-2 2C5 13 1 9 1 3z" fill="#fff"/></svg><span>(407) 555-0148</span></div>
    <div class="contact-row"><svg width="14" height="14" viewBox="0 0 14 14"><rect x="1" y="3" width="12" height="8" fill="#fff"/><polyline points="1,3 7,8 13,3" fill="none" stroke="#2e2e2e" stroke-width="1.2"/></svg><span>info@amberlinepw.com</span></div>
  </div>
  <div class="foot-col" style="left:394px;width:150px">
    <h5>Information</h5>
    <ul><li>Specials</li><li>New products</li><li>Best sellers</li><li>Our stores</li></ul>
  </div>
  <div class="foot-col" style="left:557px;top:56px;width:150px">
    <ul><li>Contact us</li><li>Pages configuration</li><li>Sitemap</li></ul>
  </div>
  <div class="foot-col" style="left:787px;width:240px">
    <h5>Subscribe</h5>
    <div>us an regione epicuri suscipiantur, sit<br>luptatum urbanitas</div>
    <div class="subscribe-input">enter email address</div>
    <div><span class="subscribe-btn">Submit</span><span style="display:inline-block;width:150px;line-height:1.3">us an regione epicuri suscipiantur, sit luptatum</span></div>
  </div>
</footer>

<section class="copyright">Copyright 2014 All rights reserved.</section>

</body>
</html>
```